Australian IT Company New Logo Business Cards Required

We are a computer consultancy / MSP located in Brisbane Australia looking to have business cards designed with our new logo, we are looking for something professional that catches the eye.
I can provide the logo in other formats if required, let's see what you can create!

```html
<!DOCTYPE html>
<html lang="en">
<head>
<meta charset="utf-8">
<title>Nevaro Business Card</title>
<link href="https://fonts.googleapis.com/css2?family=Lato:wght@400;700;900&display=swap" rel="stylesheet">
<style>
  :root {
    --backdrop: #e7e1d8;
    --card: #f2eee8;
    --card-edge: #ddd6cc;
    --panel-grey: #8e8b87;
    --panel-green: #8cc43f;
    --brand-green: #7dbb34;
    --name-green: #97cf48;
    --title-light: #eeeeea;
    --contact-light: #f4f8ee;
    --tagline-grey: #7c7a77;
  }
  * { margin: 0; padding: 0; box-sizing: border-box; }
  html, body {
    width: 1200px;
    height: 1047px;
    overflow: hidden;
    background: var(--backdrop);
    font-family: "Lato", sans-serif;
  }
  .card {
    position: absolute;
    left: 80px;
    top: 242px;
    width: 1040px;
    height: 562px;
    background: var(--card);
    border: 1px solid var(--card-edge);
    border-radius: 22px;
    overflow: hidden;
    box-shadow: 0 10px 30px rgba(0,0,0,0.08);
  }
  .identity-panel {
    position: absolute;
    left: 0;
    top: 0;
    width: 500px;
    height: 272px;
    background: var(--panel-grey);
    border-bottom-right-radius: 16px;
  }
  .person-name {
    position: absolute;
    left: 75px;
    top: 94px;
    font-weight: 700;
    font-size: 45px;
    letter-spacing: 1px;
    color: var(--name-green);
  }
  .person-title {
    position: absolute;
    left: 75px;
    top: 156px;
    font-size: 25px;
    color: var(--title-light);
  }
  .contact-panel {
    position: absolute;
    left: 0;
    top: 288px;
    width: 495px;
    height: 274px;
    background: var(--panel-green);
    border-top-right-radius: 16px;
    color: var(--contact-light);
  }
  .address {
    position: absolute;
    left: 67px;
    top: 44px;
    font-size: 26px;
    line-height: 34px;
  }
  .contact-list {
    position: absolute;
    left: 67px;
    top: 130px;
    list-style: none;
    font-size: 26px;
  }
  .contact-list li {
    display: flex;
    align-items: center;
    height: 38px;
  }
  .contact-list svg {
    width: 26px;
    height: 26px;
    margin-right: 24px;
    flex: none;
  }
  .brand {
    position: absolute;
    left: 570px;
    top: 238px;
    width: 440px;
  }
  .brand-line {
    display: flex;
    align-items: center;
    gap: 14px;
  }
  .brand-dot {
    width: 30px;
    height: 30px;
    border-radius: 50%;
    background: var(--brand-green);
  }
  .brand-name {
    font-weight: 900;
    font-size: 58px;
    letter-spacing: 2px;
    color: var(--brand-green);
    line-height: 1;
  }
  .brand-tagline {
    margin-top: 10px;
    font-weight: 700;
    font-size: 17.5px;
    letter-spacing: 1.4px;
    color: var(--tagline-grey);
  }
</style>
</head>
<body>
  <div class="card">
    <div class="identity-panel">
      <div class="person-name">JOHN SMITH</div>
      <div class="person-title">Founder &amp; CEO</div>
    </div>

    <div class="contact-panel">
      <div class="address">
        1234 First Line Address<br>
        5678 Second Line Address
      </div>
      <ul class="contact-list">
        <li>
          <svg viewBox="0 0 24 24" fill="none" stroke="currentColor" stroke-width="2" stroke-linecap="round" stroke-linejoin="round" aria-hidden="true">
            <path d="M5 3h4l2 5-2.5 1.5a11 11 0 0 0 6 6L16 13l5 2v4a2 2 0 0 1-2 2A16 16 0 0 1 3 5a2 2 0 0 1 2-2z"/>
          </svg>
          1234567890
        </li>
        <li>
          <svg viewBox="0 0 24 24" fill="currentColor" aria-hidden="true">
            <path d="M2 5h20v14H2z M3 6l9 7 9-7" fill="currentColor"/>
            <path d="M2.5 5.5l9.5 7.5 9.5-7.5" fill="none" stroke="#8cc43f" stroke-width="1.6"/>
          </svg>
          info@yourmail.com
        </li>
        <li>
          <svg viewBox="0 0 24 24" fill="none" stroke="currentColor" stroke-width="1.8" aria-hidden="true">
            <circle cx="12" cy="12" r="9"/>
            <path d="M3 12h18M12 3c3 3 3 15 0 18M12 3c-3 3-3 15 0 18"/>
          </svg>
          www.yourwebsite.com
        </li>
      </ul>
    </div>

    <div class="brand">
      <div class="brand-line">
        <span class="brand-dot"></span>
        <span class="brand-name">NEVARO</span>
      </div>
      <div class="brand-tagline">IT SOLUTIONS FOR SMALL BUSINESS</div>
    </div>
  </div>
</body>
</html>
```